Tolvik cards

I want a simple business card that pops.
Logo on one side.
On side two i want.
"Are you thinking about a new building on your property, or renovating an existing structure? Contact".....
Owners Name: Gary Pellman
Owners Phone number: 555-209-4176
Address:4716 Copper Fern RD, Ashvale, OH 44190
Committed to Quality, Service, and Integrity

```html
<!DOCTYPE html>
<html lang="en">
<head>
<meta charset="utf-8">
<title>Tolvik Builders LLC – Business Card</title>
<link rel="stylesheet" href="https://fonts.googleapis.com/css2?family=Bebas+Neue&family=Montserrat:wght@600;700&family=Poppins:wght@400&display=swap">
<style>
  :root {
    --page-bg: #d8d2cf;
    --card-bg: #efeae8;
    --brown: #3f2e1f;
    --white: #ffffff;
  }
  * { margin: 0; padding: 0; box-sizing: border-box; }
  html, body {
    width: 1200px;
    height: 900px;
    overflow: hidden;
    background: var(--page-bg);
  }
  .card {
    position: absolute;
    left: 100px;
    top: 140px;
    width: 1000px;
    height: 620px;
    background: var(--card-bg);
    box-shadow: 0 10px 30px rgba(0,0,0,0.12);
  }
  .question-panel {
    position: absolute;
    left: 35px;
    top: 73px;
    width: 418px;
    height: 466px;
  }
  .question-panel svg { display: block; }
  .question-text {
    position: absolute;
    left: 60px;
    top: 250px;
    width: 380px;
    font-family: "Bebas Neue", sans-serif;
    font-size: 44px;
    line-height: 55px;
    color: var(--white);
    white-space: nowrap;
  }
  .brand {
    position: absolute;
    left: 500px;
    top: 100px;
    width: 440px;
    display: flex;
    align-items: center;
    justify-content: center;
    gap: 14px;
  }
  .brand-mark {
    width: 44px;
    height: 44px;
    background: var(--brown);
  }
  .brand-name {
    font-family: "Montserrat", sans-serif;
    font-weight: 700;
    font-size: 31px;
    color: var(--brown);
    letter-spacing: 0.5px;
    white-space: nowrap;
  }
  .contact {
    position: absolute;
    left: 517px;
    top: 252px;
    width: 410px;
    text-align: center;
    color: var(--brown);
  }
  .contact-label {
    display: flex;
    align-items: center;
    gap: 12px;
    font-family: "Poppins", sans-serif;
    font-size: 27px;
    height: 40px;
  }
  .contact-label::before,
  .contact-label::after {
    content: "";
    flex: 1;
    height: 2px;
    background: var(--brown);
  }
  .contact-name {
    margin-top: 6px;
    font-family: "Montserrat", sans-serif;
    font-weight: 700;
    font-size: 37px;
    line-height: 46px;
  }
  .contact-phone {
    font-family: "Poppins", sans-serif;
    font-size: 27px;
    line-height: 40px;
  }
  .contact-address {
    margin-top: 10px;
    font-family: "Poppins", sans-serif;
    font-size: 27px;
    line-height: 37px;
  }
  .divider {
    position: absolute;
    left: 519px;
    top: 488px;
    width: 406px;
    height: 2px;
    background: var(--brown);
  }
  .tagline {
    position: absolute;
    left: 500px;
    top: 507px;
    width: 444px;
    text-align: center;
    font-family: "Bebas Neue", sans-serif;
    font-size: 29px;
    color: var(--brown);
    white-space: nowrap;
  }
</style>
</head>
<body>
  <main class="card">
    <div class="question-panel">
      <svg width="418" height="466" viewBox="0 0 418 466" aria-hidden="true">
        <polygon points="0,0 418,136 418,466 0,466" fill="var(--brown)"/>
      </svg>
    </div>
    <p class="question-text">Are you thinking about<br>a new building on your<br>property, or renovating<br>an existing structure?</p>

    <div class="brand">
      <span class="brand-mark" aria-hidden="true"></span>
      <span class="brand-name">TOLVIK BUILDERS LLC</span>
    </div>

    <section class="contact">
      <p class="contact-label">Contact</p>
      <p class="contact-name">GARY PELLMAN</p>
      <p class="contact-phone">555-209-4176</p>
      <p class="contact-address">4716 Copper Fern RD,<br>Ashvale, OH 44190</p>
    </section>

    <div class="divider"></div>
    <p class="tagline">Committed to Quality, Service and Integrity</p>
  </main>
</body>
</html>
```